Harbor Learning Center Posters Showing Building Blocks

We need poster designs for a School in Arizona for kids with Autism. There will be 4 such posters needed which highlight our schools building blocks. Requirements for all 4 posters are as followed: 1) We need the Harbor Learning Center Logo on each poster. I have included attachment. 2) The posters need the following titles: Building Block #1 (for the first poster), Building Block #2 for the 2nd poster, Building Block #3 for the 3rd poster, and Building Block #4 for the forth poster. 3) The main text and focus of the posters will be the following key words: For the first poster the words "Kids first in every decision". The words for the second poster are: "Students are friends with each other, and welcome new students with open arms." The words for the 3rd poster are: "The school is quiet, and students are working hard to do their best." The words for the 4th poster are: "Parents see amazing improvement in their child." 4) We would love to use some of the kids art from our schools if possible. Use your expertise to decide. I will send these out as well. 5) Try and design the posters around the key words from each poster 6) I am sure if landscape or portrait would be best so I will let the experts decide. All 4 posters need to be the same layout once decided.

Target Market(s)

These posters are for the school only. Prospective students/parents will see these posters so they will be used for Marketing from that perspective. We may put out into local community in future.

Industry/Entity Type

School

Font styles to use
Serif

Requirements
Must have
• 1) Logo (Harbor Learning Center for Growth and Discovery)
• 2) Title: as described in write up
• 3) Key words: as described in write up
Nice to have
• Kids art from school. Note: This is the first time that I have been on this site so I may have made a mistake by putting 4 posters on one project. I am assuming that I would need to pay more to have 4 posters so let me know if I need to modify the project in any way?

```html
<!DOCTYPE html>
<html lang="en">
<head>
<meta charset="utf-8">
<title>Harbor Learning Center – Building Block #4</title>
<link rel="stylesheet" href="https://fonts.googleapis.com/css2?family=Bangers&family=Tinos:wght@400;700&display=swap">
<style>
  :root {
    --page-bg: #d9d6d2;
    --paper: #f7f7f5;
    --board: #2c2e30;
    --board-light: #3a3d3f;
    --chalk: #ecebe8;
    --wood-dark: #3b2516;
    --wood: #5a3a24;
    --art-warm: #f2b04a;
    --art-cool: #5a7fd0;
    --art-pink: #e86aa3;
    --brand-ink: #141414;
    --brand-accent: #c9262b;
  }
  * { box-sizing: border-box; margin: 0; padding: 0; }
  html, body {
    width: 923px; height: 1200px; overflow: hidden;
    background: var(--page-bg);
  }
  .poster {
    position: absolute; left: 33px; top: 0;
    width: 857px; height: 1200px;
    background: var(--paper);
  }
  .chalkboard {
    position: absolute; left: 22px; top: 20px; right: 22px; bottom: 26px;
    background:
      radial-gradient(ellipse at 50% 45%, var(--board-light) 0%, var(--board) 70%);
  }
  .series-title {
    position: absolute; top: 62px; left: 0; right: 0;
    text-align: center;
    font-family: "Tinos", "Times New Roman", serif;
    font-weight: 700; font-size: 17px; letter-spacing: 0.3px;
    color: var(--chalk);
  }
  .art-frame {
    position: absolute; left: 78px; top: 120px;
    width: 668px; height: 447px;
    border: 18px solid var(--wood);
    border-color: var(--wood) var(--wood-dark) var(--wood-dark) var(--wood);
    box-shadow: 0 8px 14px rgba(0,0,0,0.45);
    background: var(--wood);
  }
  .art-frame .artwork {
    width: 100%; height: 100%;
    background:
      radial-gradient(circle at 20% 30%, var(--art-pink) 0%, transparent 35%),
      radial-gradient(circle at 75% 65%, var(--art-cool) 0%, transparent 40%),
      linear-gradient(120deg, var(--art-warm), #e8d7b8 50%, #9fc15c);
  }
  .key-words {
    position: absolute; top: 618px; left: 0; right: 0;
    text-align: center;
    font-family: "Bangers", "Impact", sans-serif;
    font-size: 56px; line-height: 66px; letter-spacing: 1.5px;
    color: var(--chalk);
    text-shadow: 0 0 2px rgba(255,255,255,0.25);
  }
  .brand {
    position: absolute; left: 160px; top: 880px;
    display: flex; align-items: flex-start; gap: 14px;
    color: var(--brand-ink);
    font-family: "Tinos", "Times New Roman", serif;
    font-weight: 400;
  }
  .brand-mark {
    width: 34px; height: 34px; margin-top: 4px;
    background: var(--brand-accent);
  }
  .brand-name { font-size: 30px; line-height: 36px; }
  .brand-tagline { font-size: 25px; line-height: 32px; }
</style>
</head>
<body>
  <main class="poster">
    <section class="chalkboard">
      <h2 class="series-title">BUILDING BLOCK #4</h2>
      <figure class="art-frame">
        <div class="artwork" role="img" aria-label="Student crayon drawing of overlapping colorful circles outlined in blue"></div>
      </figure>
      <h1 class="key-words">"PARENTS SEE<br>AMAZING IMPROVEMENT<br>IN THEIR CHILD."</h1>
      <div class="brand">
        <span class="brand-mark"></span>
        <div>
          <div class="brand-name">HARBOR LEARNING CENTER</div>
          <div class="brand-tagline">for Growth &amp; Discovery</div>
        </div>
      </div>
    </section>
  </main>
</body>
</html>
```